Need a business card design for a residential architect.

You can get a sense of his work at www.tbrolvik.com

Would like a consistent look and feel between business card and website
.

Target Market(s)

Residential homeowners builders

Industry/Entity Type

Residential

Contact Information for Business Card

Dale Brolvik
Principle
Brolvik Architecture
418 Quill Lane
Oakmere Park, CA 94871

dale@tbrolvik.com

tbrolvik.com
phone: 650-555-0172
Fax: 650-555-0196

Font styles to use
Sans Serif

Requirements
Must have
• Details above
Nice to have
• Would like a consistent look and feel between business card and website
Should not have
• None

```html
<!DOCTYPE html>
<html lang="en">
<head>
<meta charset="utf-8">
<title>Brolvik Architecture – Business Card</title>
<link href="https://fonts.googleapis.com/css2?family=Montserrat:wght@400;500;600&display=swap" rel="stylesheet">
<style>
  :root {
    --page-bg: #ffffff;
    --card-bg: #efefef;
    --card-edge: #d6d6d6;
    --front-light: #fafafa;
    --front-mid: #e2e2e2;
    --front-dark: #cfcfcf;
    --ink: #6b6b6b;
    --ink-strong: #555555;
    --accent: #3f8c8c;
    --band: #a9a9a9;
    --band-text: #ffffff;
    --rule: #b9b9b9;
  }
  * { box-sizing: border-box; margin: 0; padding: 0; }
  html, body {
    width: 1200px; height: 620px; overflow: hidden;
    background: var(--page-bg);
    font-family: "Montserrat", Arial, sans-serif;
  }
  .canvas { position: relative; width: 1200px; height: 620px; }
  .card {
    position: absolute; top: 154px;
    width: 540px; height: 312px;
    border: 1px solid var(--card-edge);
    box-shadow: 0 2px 6px rgba(0,0,0,0.12);
    overflow: hidden;
  }
  .card-front {
    left: 40px;
    background:
      radial-gradient(ellipse 60% 80% at 50% 70%, var(--front-light) 0%, rgba(250,250,250,0) 70%),
      linear-gradient(160deg, var(--front-mid) 0%, var(--front-light) 45%, var(--front-dark) 100%);
  }
  .front-wordmark {
    position: absolute; left: 0; right: 0; top: 96px;
    text-align: center;
    font-weight: 500; font-size: 44px; line-height: 56px;
    letter-spacing: 1px;
    color: var(--ink);
  }
  .card-back { left: 620px; background: var(--card-bg); }
  .back-wordmark {
    position: absolute; left: 30px; top: 42px; width: 216px;
    text-align: center;
    font-weight: 500; font-size: 22px; line-height: 28px;
    color: var(--ink);
  }
  .divider {
    position: absolute; left: 267px; top: 42px;
    width: 1px; height: 203px; background: var(--rule);
  }
  .address {
    position: absolute; left: 30px; top: 150px; width: 216px;
    text-align: center;
    font-size: 15px; line-height: 21px; color: var(--ink);
  }
  .contact { position: absolute; right: 28px; top: 44px; text-align: right; }
  .person-name { font-weight: 600; font-size: 20px; line-height: 24px; color: var(--ink-strong); }
  .person-role { font-size: 16px; line-height: 20px; color: var(--accent); }
  .phone-list { margin-top: 18px; list-style: none; }
  .phone-list li {
    display: flex; justify-content: flex-end; align-items: center;
    gap: 8px; height: 34px;
    font-size: 18px; color: var(--ink-strong);
  }
  .icon { width: 22px; height: 22px; display: block; }
  .email {
    position: absolute; right: 28px; top: 210px;
    display: flex; align-items: center; gap: 8px;
    font-size: 15px; color: var(--ink-strong);
  }
  .email .icon { width: 16px; height: 16px; }
  .web-band {
    position: absolute; left: 0; right: 0; top: 256px; height: 31px;
    background: var(--band);
    color: var(--band-text);
    font-size: 18px; line-height: 31px; text-align: center;
    letter-spacing: 0.5px;
  }
</style>
</head>
<body>
<main class="canvas">
  <section class="card card-front" aria-label="Card front">
    <p class="front-wordmark">Brolvik<br>Architecture</p>
  </section>

  <section class="card card-back" aria-label="Card back">
    <p class="back-wordmark">Brolvik<br>Architecture</p>
    <p class="address">418 Quill Lane<br>Oakmere Park,<br>CA 94871</p>
    <div class="divider"></div>

    <div class="contact">
      <p class="person-name">Dale Brolvik</p>
      <p class="person-role">Principal</p>
      <ul class="phone-list">
        <li>
          <svg class="icon" viewBox="0 0 22 22" aria-hidden="true">
            <circle cx="11" cy="11" r="10" fill="none" stroke="var(--accent)" stroke-width="1.5"/>
            <path d="M7.5 6.5c.6-.6 1.4-.5 1.8.1l.9 1.4c.3.5.2 1.1-.2 1.5l-.5.5c.5 1.1 1.4 2 2.5 2.5l.5-.5c.4-.4 1-.5 1.5-.2l1.4.9c.6.4.7 1.2.1 1.8l-.6.6c-.8.8-2.1.9-3.1.3-2.2-1.2-3.900-2.900-5.100-5.100-.6-1-.5-2.3.3-3.1z" fill="var(--accent)"/>
          </svg>
          <span>650-555-0172</span>
        </li>
        <li>
          <svg class="icon" viewBox="0 0 22 22" aria-hidden="true">
            <circle cx="11" cy="11" r="10" fill="none" stroke="var(--accent)" stroke-width="1.5"/>
            <rect x="6.5" y="9" width="9" height="7" rx="1" fill="var(--accent)"/>
            <rect x="8" y="5.5" width="6" height="4" fill="none" stroke="var(--accent)" stroke-width="1.2"/>
            <rect x="8.5" y="11" width="5" height="1" fill="var(--card-bg)"/>
            <rect x="8.5" y="13" width="5" height="1" fill="var(--card-bg)"/>
          </svg>
          <span>650-555-0196</span>
        </li>
      </ul>
    </div>

    <p class="email">
      <svg class="icon" viewBox="0 0 16 16" aria-hidden="true">
        <rect x="1.5" y="3.5" width="13" height="9" fill="none" stroke="var(--accent)" stroke-width="1.3"/>
        <path d="M1.5 3.5 8 9l6.5-5.5" fill="none" stroke="var(--accent)" stroke-width="1.3"/>
      </svg>
      <span>dale@tbrolvik.com</span>
    </p>

    <p class="web-band">www.tbrolvik.com</p>
  </section>
</main>
</body>
</html>
```